Dential Clinic Business Card

We need a simple elegant business card. 2 sided. First side with our details, and 2nd side with appointment time rows.

Dark background preferred. Will consider monotone design, or colored. Surprise us.

Details:
SIDE1

Harwick Plaza Dental

Dr Milo Brent
BDSc(Tarn) MOPRVS

Shop 42, Harwick Plaza
8-22 Larch Avenue, Harwick VIC 3190
Phone: 03 9447 2835
email: info@harwickplazadental.com.au
site: www.harwickplazadental.com.au
_____________________________________
SIDE 2
Appointed Time ________________________
Notes _______________________

Target Market(s)

Dental Patients

Industry/Entity Type

Healthcare

Contact Information for Business Card

SIDE1

Harwick Plaza Dental

Dr Milo Brent
Shop 42, Harwick Plaza
Phone: 03 9447 2835
SIDE 2

Font styles to use
Other font styles liked:
• Comfortaa

Requirements
Must have
• Dr Milo Brent
BDSc(Tarn) MOPRVS

Address
Phone
Email
Website
Nice to have
• Simple elegant design with our logo.
Colored logo.
Light text on dark background - Side 1
Light background so can be written on with dark pen - SIde 2
Should not have
• Too many colors

```html
<!DOCTYPE html>
<html lang="en">
<head>
<meta charset="utf-8">
<title>Harwick Plaza Dental – Business Card</title>
<link rel="stylesheet" href="https://fonts.googleapis.com/css2?family=Cutive+Mono&family=Open+Sans:ital,wght@0,400;0,600;1,400&display=swap">
<style>
  :root {
    --page-bg: #e9e9e6;
    --forest: #1b3a1e;
    --green-light: #0ba04f;
    --green-deep: #087a38;
    --tab-blue: #1f95d6;
    --logo-green: #8cc63f;
    --ink-white: #ffffff;
    --ink-soft: #d9f2e2;
    --paper: #ffffff;
    --rule-grey: #9a9a9a;
    --label-grey: #7a7a7a;
  }
  * { margin: 0; padding: 0; box-sizing: border-box; }
  html, body { width: 1200px; height: 900px; overflow: hidden; }
  body { background: var(--page-bg); position: relative; font-family: "Open Sans", sans-serif; }

  .card {
    position: absolute; left: 250px; width: 700px; height: 400px;
    border-radius: 24px; overflow: hidden;
    box-shadow: 0 8px 24px rgba(0,0,0,.18);
  }
  .card-front { top: 30px; }
  .card-back { top: 470px; background: var(--paper); }
  .card-art { position: absolute; inset: 0; }

  .brand { position: absolute; display: flex; align-items: center; gap: 12px; white-space: nowrap; }
  .brand-dot { width: 24px; height: 24px; border-radius: 50%; background: var(--logo-green); flex: none; }
  .brand-name { color: var(--logo-green); font-weight: 600; font-size: 22px; letter-spacing: 1px; line-height: 1; }
  .card-front .brand { left: 95px; top: 205px; transform: translate(-50%, -50%) rotate(-90deg); }
  .card-back .brand { left: 50%; top: 340px; transform: translate(-50%, -50%); }

  .doctor { position: absolute; left: 280px; top: 56px; }
  .doctor-name {
    font-family: "Cutive Mono", monospace; font-weight: 400; font-size: 32px; letter-spacing: 8px;
    line-height: 40px; color: var(--ink-white); white-space: nowrap;
  }
  .doctor-credentials {
    margin-top: 4px; font-size: 15px; font-weight: 400; letter-spacing: 2px;
    color: var(--ink-soft); white-space: nowrap;
  }
  .contact-list { position: absolute; left: 240px; top: 170px; list-style: none; }
  .contact-list li { color: var(--ink-white); font-weight: 600; font-size: 18px; line-height: 34px; white-space: nowrap; }

  .appointment-rows { position: absolute; left: 50px; right: 50px; top: 30px; }
  .appointment-row { display: flex; align-items: flex-end; gap: 8px; height: 56px; }
  .appointment-row .label { font-style: italic; font-size: 14px; color: var(--label-grey); white-space: nowrap; }
  .appointment-row .rule { flex: 1; border-bottom: 1px solid var(--rule-grey); margin-bottom: 4px; }
</style>
</head>
<body>

<section class="card card-front" aria-label="Front of business card">
  <svg class="card-art" width="700" height="400" viewBox="0 0 700 400" aria-hidden="true">
    <defs>
      <linearGradient id="front-green" x1="0" y1="0" x2="1" y2="1">
        <stop offset="0" stop-color="#0ba04f"/>
        <stop offset="1" stop-color="#087a38"/>
      </linearGradient>
    </defs>
    <rect width="700" height="400" fill="url(#front-green)"/>
    <path d="M0 0 H240 V130 H195 V400 H0 Z" fill="#1b3a1e"/>
    <rect x="210" y="40" width="50" height="80" rx="14" fill="#1f95d6"/>
    <circle cx="235" cy="78" r="13" fill="#ffffff"/>
    <circle cx="235" cy="74" r="4" fill="#1f95d6"/>
    <path d="M228 85 a7 6 0 0 1 14 0 Z" fill="#1f95d6"/>
    <rect x="170" y="160" width="52" height="230" rx="16" fill="#1f95d6"/>
    <g fill="none" stroke="#ffffff" stroke-width="1.6">
      <circle cx="196" cy="187" r="11"/>
      <circle cx="196" cy="221" r="11"/>
      <circle cx="196" cy="255" r="11"/>
      <circle cx="196" cy="306" r="11"/>
    </g>
    <path d="M192 182 q-2 5 3 10 q5 5 9 3 l-2 -3 l-3 1 q-3 -2 -5 -5 l1 -3 Z" fill="#ffffff"/>
    <rect x="189" y="216" width="14" height="10" fill="none" stroke="#ffffff" stroke-width="1.4"/>
    <path d="M189 216 l7 6 l7 -6" fill="none" stroke="#ffffff" stroke-width="1.4"/>
    <path d="M190 258 l12 -8 l-4 13 l-2 -4 Z" fill="#ffffff"/>
    <path d="M196 313 q-6 -7 -6 -11 a6 6 0 0 1 12 0 q0 4 -6 11 Z" fill="#ffffff"/>
    <circle cx="196" cy="302" r="2" fill="#1f95d6"/>
  </svg>

  <div class="brand">
    <span class="brand-dot"></span>
    <span class="brand-name">HARWICK PLAZA DENTAL</span>
  </div>

  <div class="doctor">
    <h1 class="doctor-name">Dr Milo Brent</h1>
    <p class="doctor-credentials">BDSc(Tarn) MOPRVS</p>
  </div>

  <ul class="contact-list">
    <li>03 9447 2835</li>
    <li>info@harwickplazadental.com.au</li>
    <li>www.harwickplazadental.com.au</li>
    <li>Shop 42, Harwick Plaza</li>
    <li>8-22 Larch Avenue, Harwick VIC 3190</li>
  </ul>
</section>

<section class="card card-back" aria-label="Back of business card">
  <svg class="card-art" width="700" height="400" viewBox="0 0 700 400" aria-hidden="true">
    <rect width="700" height="400" fill="#ffffff"/>
    <rect y="280" width="700" height="120" fill="#1b3a1e"/>
  </svg>

  <div class="appointment-rows">
    <div class="appointment-row"><span class="label">Appointed Time</span><span class="rule"></span></div>
    <div class="appointment-row"><span class="label">Notes</span><span class="rule"></span></div>
    <div class="appointment-row"><span class="label">Appointed Time</span><span class="rule"></span></div>
    <div class="appointment-row"><span class="label">Notes</span><span class="rule"></span></div>
  </div>

  <div class="brand">
    <span class="brand-dot"></span>
    <span class="brand-name">HARWICK PLAZA DENTAL</span>
  </div>
</section>

</body>
</html>
```